Looking for a modern, Professional business card design

We have a simple business card, but are looking for a more modern, professional look. A sample of the basic card is attached as well as the logo. We would also like to add that we offer:
Struggling with your finances?
- Learn to become debt free
- Discover the power of cash
- Control your money instead of it controlling you
Let us help you achieve a new level of financial freedom!
Also, we would like to have a "SPECIAL OFFER!: FREE 30 minute consultation"
Financial Planning

```html
<!DOCTYPE html>
<html lang="en">
<head>
<meta charset="utf-8">
<title>Liberty Money Coaching – Business Card</title>
<link rel="stylesheet" href="https://fonts.googleapis.com/css2?family=Roboto:wght@400;500;700&display=swap">
<style>
  :root {
    --bg: #3a3b3d;
    --card-white: #ffffff;
    --card-black: #0b0b0b;
    --green-dark: #3d8a1f;
    --green: #5aa82a;
    --green-light: #9fd04f;
    --text-light: #ffffff;
    --text-grey: #c9c9c9;
    --text-dark: #1d1d1d;
  }
  * { box-sizing: border-box; margin: 0; padding: 0; }
  html, body {
    width: 1200px; height: 950px; overflow: hidden;
    background: var(--bg);
    font-family: "Roboto", Arial, sans-serif;
  }
  .stage {
    width: 1200px; height: 950px;
    display: flex; flex-direction: column; align-items: center; justify-content: center;
    gap: 50px;
  }
  .card {
    position: relative; width: 700px; height: 400px; overflow: hidden;
    border-radius: 4px; box-shadow: 0 10px 30px rgba(0,0,0,.45);
  }

  /* Back card */
  .card--back { background: var(--card-black); color: var(--text-grey); }
  .card--back .brand { position: absolute; top: 60px; left: 0; right: 0; text-align: center; }
  .brand-name {
    display: inline-flex; align-items: center; gap: 14px;
    font-weight: 700; text-transform: uppercase; letter-spacing: 1px;
  }
  .brand-mark { width: 22px; height: 22px; border-radius: 50%; flex: none; }
  .card--back .brand-name { font-size: 34px; color: var(--text-light); }
  .card--back .brand-mark { background: var(--text-light); }
  .brand-tagline { font-size: 12px; margin-top: 6px; letter-spacing: .5px; }
  .card--back .brand-tagline { color: var(--text-grey); }
  .pitch { position: absolute; top: 175px; left: 70px; right: 70px; font-size: 17px; line-height: 1.55; }
  .pitch-title { font-weight: 700; color: var(--text-light); text-transform: uppercase; font-size: 18px; margin-bottom: 4px; }
  .pitch-list { list-style: none; }
  .pitch-list li::before { content: "• "; color: var(--green-light); }
  .pitch-offer { margin-top: 14px; font-size: 19px; color: var(--text-light); font-weight: 500; }
  .pitch-offer strong { color: var(--green-light); font-weight: 700; }

  /* Front card */
  .card--front { background: var(--card-white); }
  .swoosh { position: absolute; inset: 0; width: 700px; height: 400px; }
  .card--front .brand { position: absolute; top: 48px; left: 44px; }
  .card--front .brand-name { font-size: 30px; color: var(--green-dark); }
  .card--front .brand-mark { background: var(--green); }
  .card--front .brand-tagline { color: #555; margin-left: 36px; }
  .contact {
    position: absolute; right: 40px; bottom: 34px; text-align: right;
    color: var(--text-light); font-size: 18px; line-height: 1.45;
  }
  .contact-name { font-size: 24px; font-weight: 500; }
  .contact-role { margin-bottom: 10px; }
  .contact-label { font-weight: 700; }
</style>
</head>
<body>
<main class="stage">

  <section class="card card--back" aria-label="Business card back">
    <div class="brand">
      <div class="brand-name"><span class="brand-mark"></span>Liberty Money Coaching</div>
      <p class="brand-tagline">Achieve a new level of personal freedom</p>
    </div>
    <div class="pitch">
      <p class="pitch-title">Struggling with your finances?</p>
      <ul class="pitch-list">
        <li>Learn to become debt free &nbsp;• Discover the power of cash</li>
        <li>Control your money instead of it controlling you</li>
      </ul>
      <p>Let us help you achieve a new level of financial freedom!</p>
      <p class="pitch-offer"><strong>SPECIAL OFFER!:</strong> FREE 30 minute consultation</p>
    </div>
  </section>

  <section class="card card--front" aria-label="Business card front">
    <svg class="swoosh" viewBox="0 0 700 400" role="img" aria-label="Large green swooping brand graphic across the lower right of the card">
      <defs>
        <linearGradient id="swooshFill" x1="0" y1="0" x2="1" y2="1">
          <stop offset="0" stop-color="#9fd04f"/>
          <stop offset=".5" stop-color="#5aa82a"/>
          <stop offset="1" stop-color="#3d8a1f"/>
        </linearGradient>
      </defs>
      <path d="M230 400 C 260 260, 330 160, 420 150 C 520 150, 620 200, 700 250 L 700 400 Z" fill="url(#swooshFill)"/>
    </svg>
    <div class="brand">
      <div class="brand-name"><span class="brand-mark"></span>Liberty Money Coaching</div>
      <p class="brand-tagline">Achieve a new level of personal freedom</p>
    </div>
    <address class="contact" style="font-style:normal">
      <p class="contact-name">Daniel R. Hayes</p>
      <p class="contact-role">Personal Financial Coach</p>
      <p><span class="contact-label">Mob:</span> (205) 555-0187</p>
      <p>daniel@steadymoneypath.com</p>
      <p>www.steadymoneypath.com</p>
    </address>
  </section>

</main>
</body>
</html>
```